Lantern & Plates Jamboree flyer/logo concept

Flyer/logo concept that we can use for our annual festival. This is the 3rd annual event.
Featuring deacon Marlow blaze, Tillbrook Row, Otter ridge, and more to be added. June 16-17 2017 Pellham county showgrounds. Brackton Ohio 45820
www.lanternplatesjam.example We will have food trucks, camping and beer available as well as 9 bands Leave space to add bands and add sponsors
ALSO visit our facebook page for other photos and insipiration
Updates

DO not use previous logo's. All of the attached info is for reference only. I want a fresh logo that can be used throughout the campaign. I can copy and paste my own items so please..........be fresh and creative......

Target Market(s)

18-60 Rockabilly , food truck , southern rock country vibe

Industry/Entity Type

Festival

Requirements
Must have
• website- dates- Camping-music-beer-food.
Nice to have
• File or logo that can also be used on a shirt See our website and facebook pages
Should not have
• UPDATE 1-20-17 I only included the previous logo's for reference. I do NOT want to use old logo. I would have done it myself if that was the case. Be creative, give me something I can use and also work with for shirts and stickers etc. That's what the previous logos were.

```html
<!DOCTYPE html>
<html lang="en">
<head>
<meta charset="utf-8">
<title>Lantern &amp; Plates Jamboree — Flyer</title>
<link rel="stylesheet" href="https://fonts.googleapis.com/css2?family=Open+Sans:wght@400;700&family=Poiret+One&family=Architects+Daughter&display=swap">
<style>
  :root {
    --page: #d9d9d6;
    --flyer: #2d2926;
    --ink: #ece6dc;
    --ink-soft: #bdb6ab;
    --green: #7a8a2e;
    --red: #c9262d;
    --orange: #e9a62a;
  }
  * { margin: 0; padding: 0; box-sizing: border-box; }
  html, body { width: 1200px; height: 900px; overflow: hidden; }
  body {
    background: var(--page);
    font-family: "Open Sans", sans-serif;
    position: relative;
  }
  .flyer {
    position: absolute;
    left: 320px; top: 55px;
    width: 560px; height: 790px;
    background: var(--flyer);
    color: var(--ink);
    box-shadow: 0 10px 30px rgba(0,0,0,.25);
  }
  .brand {
    position: absolute; top: 28px; left: 0; width: 100%;
    text-align: center;
  }
  .brand__dot {
    width: 80px; height: 80px; border-radius: 50%;
    background: var(--orange); margin: 0 auto 12px;
  }
  .brand__name {
    font-weight: 700; color: var(--red);
    font-size: 34px; line-height: 38px;
    text-transform: uppercase; letter-spacing: 2px;
  }
  .brand__edition {
    margin-top: 8px; font-size: 18px; line-height: 24px;
    letter-spacing: 2px; color: var(--ink);
  }
  .perk {
    position: absolute; font-size: 14px; line-height: 20px;
    letter-spacing: 1px; color: var(--ink); text-transform: uppercase;
  }
  .perk--beer { right: 100px; top: 232px; }
  .perk--trucks { left: 55px; top: 276px; }
  .perk--bands { right: 55px; top: 270px; }
  .perk--camping { left: 70px; top: 332px; }
  .featuring {
    position: absolute; left: 50%; top: 292px; transform: translateX(-50%);
    background: var(--red); color: var(--ink);
    font-weight: 700; font-size: 13px; line-height: 18px; letter-spacing: 4px;
    padding: 4px 22px; text-transform: uppercase;
  }
  .lineup {
    position: absolute; top: 330px; left: 0; width: 100%;
    list-style: none; text-align: center;
    font-family: "Poiret One", sans-serif; text-transform: uppercase;
  }
  .lineup__act { font-size: 36px; letter-spacing: 8px; line-height: 46px; }
  .lineup__more { font-size: 20px; letter-spacing: 6px; line-height: 34px; }
  .details {
    position: absolute; left: 0; top: 562px; width: 100%; height: 122px;
    background: var(--green);
    font-family: "Architects Daughter", sans-serif;
    text-align: center; text-transform: uppercase;
    font-size: 22px; line-height: 30px; padding-top: 16px;
  }
  .sponsors {
    position: absolute; left: 30px; right: 30px; top: 704px;
    display: flex; justify-content: space-between; align-items: center;
    font-size: 10px; line-height: 22px; color: var(--ink-soft); text-transform: uppercase;
  }
  .sponsors__badge { width: 22px; height: 22px; border-radius: 50%; background: var(--ink-soft); }
  .contact {
    position: absolute; left: 30px; right: 30px; top: 746px;
    display: flex; justify-content: space-between; align-items: center;
    font-size: 13px; line-height: 18px; text-transform: uppercase; letter-spacing: .5px;
  }
  .contact__item { display: flex; align-items: center; gap: 8px; }
  .contact__square { width: 16px; height: 16px; background: var(--ink-soft); }
</style>
</head>
<body>
  <article class="flyer">
    <header class="brand">
      <div class="brand__dot"></div>
      <h1 class="brand__name">Lantern &amp; Plates<br>Jamboree</h1>
      <p class="brand__edition">3RD ANNUAL</p>
    </header>

    <span class="perk perk--beer">Beer</span>
    <span class="perk perk--trucks">Food Trucks</span>
    <span class="perk perk--bands">9 Bands</span>
    <span class="perk perk--camping">Camping</span>

    <div class="featuring">Featuring</div>

    <ul class="lineup">
      <li class="lineup__act">Deacon</li>
      <li class="lineup__act">Marlow Blaze</li>
      <li class="lineup__act">Tillbrook Row</li>
      <li class="lineup__act">Otter Ridge</li>
      <li class="lineup__more">And more...</li>
    </ul>

    <section class="details">
      <p>June 16-17 2017</p>
      <p>Pellham County Showgrounds,</p>
      <p>Brackton Ohio 45820</p>
    </section>

    <div class="sponsors">
      <span>Hollis Orchard</span>
      <span>KTRV</span>
      <span>Dale Fenwick</span>
      <span class="sponsors__badge"></span>
      <span>Maple Trust Bank</span>
      <span>Brookline</span>
      <span>Ridgeway Bank</span>
    </div>

    <footer class="contact">
      <span class="contact__item">
        <svg width="16" height="16" viewBox="0 0 16 16" aria-hidden="true"><path d="M2 8 L8 2 L14 8 V14 H10 V10 H6 V14 H2 Z" fill="#bdb6ab"/></svg>
        www.lanternplatesjam.example
      </span>
      <span class="contact__item">
        <span class="contact__square"></span>
        lantern-plates-jamboree
      </span>
    </footer>
  </article>
</body>
</html>
```